Professional Business Cards

We need a nice looking, profession and modern business card for our new company. Our logo is attatched

Target Market(s)

Young Professionals

Industry/Entity Type

Financial

Contact Information for Business Card

FRONT

Morvane Tally Pty Ltd
Level 22, Halden Court, 48 Wirrapool St
Sydney NSW 2000
ABN : 57 304 918 226

Derek Wallis - Chief Operations Officer
P : 02 7153 2819
M: 0418 395 207
derek@morvanetally,com

BACK

- Cryptocurrency Exchange Services
- Cryptocurrency Mining Operations
- Cryptocurrency Investment Fund Offering

Font styles to use
Sans Serif

Colors
0255a3
9d9d9d

```html
<!DOCTYPE html>
<html lang="en">
<head>
<meta charset="utf-8">
<title>Morvane Tally – Business Card</title>
<link rel="stylesheet" href="https://fonts.googleapis.com/css2?family=Saira:wght@400;600&display=swap">
<style>
  :root {
    --brand-blue: #0255a3;
    --brand-grey: #9d9d9d;
    --text-grey: #6a6a6a;
    --paper: #ffffff;
    --backdrop: #e4e4e4;
  }
  html, body {
    margin: 0;
    padding: 0;
    width: 1200px;
    height: 1000px;
    overflow: hidden;
    background: var(--backdrop);
    font-family: "Saira", sans-serif;
  }
  .canvas {
    position: relative;
    width: 1200px;
    height: 1000px;
  }
  .card {
    position: absolute;
    left: 240px;
    width: 697px;
    height: 397px;
    border-radius: 22px;
    overflow: hidden;
  }
  .card--front { top: 83px; background: var(--paper); }
  .card--back  { top: 520px; background: var(--brand-blue); }

  .holder-name {
    position: absolute; left: 45px; top: 68px; margin: 0;
    font-size: 20px; font-weight: 600; letter-spacing: 1px;
    color: var(--brand-blue); line-height: 1;
  }
  .holder-title {
    position: absolute; left: 45px; top: 94px; margin: 0;
    font-size: 14px; font-weight: 400; color: var(--text-grey); line-height: 1;
  }
  .contact-list {
    position: absolute; left: 45px; top: 164px; margin: 0; padding: 0;
    list-style: none;
  }
  .contact-list li {
    display: flex; align-items: center; height: 22.5px;
    font-size: 15px; color: var(--text-grey); letter-spacing: 0.6px;
  }
  .contact-list svg { width: 12px; height: 12px; margin-right: 12px; fill: var(--brand-blue); }
  .company-name {
    position: absolute; left: 45px; top: 270px; margin: 0;
    font-size: 15px; font-weight: 600; letter-spacing: 1px;
    color: var(--brand-blue); line-height: 1;
  }
  .company-address {
    position: absolute; left: 45px; top: 291px; margin: 0;
    font-size: 15px; color: var(--text-grey); letter-spacing: 0.6px;
    font-style: normal; line-height: 20px;
  }
  .brand-lockup {
    position: absolute; display: flex; align-items: center; gap: 12px;
    font-size: 30px; font-weight: 600; letter-spacing: 1px; line-height: 1;
  }
  .brand-lockup .brand-square { width: 22px; height: 22px; }
  .card--front .brand-lockup { right: 32px; top: 270px; color: var(--brand-blue); }
  .card--front .brand-square { background: var(--brand-blue); }
  .card--back .brand-lockup { left: 50%; top: 172px; transform: translateX(-50%); color: var(--paper); white-space: nowrap; }
  .card--back .brand-square { background: var(--paper); }

  .footer-band { position: absolute; left: 0; top: 0; width: 697px; height: 397px; }
  .abn {
    position: absolute; left: 458px; top: 370px; margin: 0;
    font-size: 14px; color: var(--paper); letter-spacing: 0.6px; line-height: 1;
  }
  .services {
    position: absolute; left: 0; right: 0; top: 316px; margin: 0;
    text-align: center; font-size: 15px; color: var(--paper);
    letter-spacing: 0.6px; line-height: 22px;
  }
</style>
</head>
<body>
<main class="canvas">
  <section class="card card--front">
    <svg class="footer-band" viewBox="0 0 697 397" aria-hidden="true">
      <path d="M0 373 H398 Q412 373 422 369 L426 377 H0 Z" fill="var(--brand-grey)"/>
      <path d="M0 382 H392 C420 382 428 365 462 365 H697 V397 H0 Z" fill="var(--brand-blue)"/>
    </svg>

    <h1 class="holder-name">DEREK WALLIS</h1>
    <p class="holder-title">Chief Operations Officer</p>

    <ul class="contact-list">
      <li><svg viewBox="0 0 24 24"><path d="M6.6 10.8a15 15 0 0 0 6.6 6.6l2.2-2.2a1 1 0 0 1 1-.25 11.4 11.4 0 0 0 3.6.57 1 1 0 0 1 1 1V20a1 1 0 0 1-1 1A17 17 0 0 1 3 4a1 1 0 0 1 1-1h3.5a1 1 0 0 1 1 1c0 1.25.2 2.45.57 3.6a1 1 0 0 1-.25 1z"/></svg>02 7153 2819</li>
      <li><svg viewBox="0 0 24 24"><path d="M7 1h10a2 2 0 0 1 2 2v18a2 2 0 0 1-2 2H7a2 2 0 0 1-2-2V3a2 2 0 0 1 2-2zm0 3v14h10V4zm5 15.5a1.2 1.2 0 1 0 0 2.4 1.2 1.2 0 0 0 0-2.4z"/></svg>0418 395 207</li>
      <li><svg viewBox="0 0 24 24"><path d="M2 5h20v2l-10 6L2 7zm0 4 10 6 10-6v10H2z"/></svg>derek@morvanetally.com</li>
    </ul>

    <h2 class="company-name">MORVANE TALLY PTY LTD</h2>
    <address class="company-address">Level 22, Halden Court, 48<br>Wirrapool St Sydney NSW 2000</address>

    <div class="brand-lockup"><span class="brand-square"></span>MORVANE TALLY</div>

    <p class="abn">ABN : 57 304 918 226</p>
  </section>

  <section class="card card--back">
    <div class="brand-lockup"><span class="brand-square"></span>MORVANE TALLY</div>
    <p class="services">Cryptocurrency Mining Operations | Cryptocurrency Exchange Services<br>Cryptocurrency Investment Fund Offering</p>
  </section>
</main>
</body>
</html>
```